Communications Contractor Business Card Design

I would like a new business card for a new Communications company in Australia. Subcontracting and specialising in cabling, data, phone, antennas, pay tv ,modems, audio visual fibre optics etc. I am open to colour and design concepts but would like a modern clean look that stands out.

Industry/Entity Type

Tv

Contact Information for Business Card

kestrel communications pty ltd, Doug Pemberton, PO BOX 657 Marlow Flats QLD 4873 kestrel4me@maildrop-example.com Australia. ph 0437196084. Director/Technician. services- Cabling,data,phone,antennas,audio visual,home theatre, fibre optics.

```html
<!DOCTYPE html>
<html lang="en">
<head>
<meta charset="utf-8">
<title>Kestrel Communications – Business Card</title>
<link rel="stylesheet" href="https://fonts.googleapis.com/css2?family=Noto+Sans:wght@400;700&display=swap">
<style>
  :root {
    --backdrop: #8c8c8c;
    --card-light: #ffffff;
    --card-shade: #e6e7e8;
    --brand-blue: #0a6aa8;
    --ink: #4a4a4a;
    --ink-soft: #5a5a5a;
  }
  * { box-sizing: border-box; margin: 0; padding: 0; }
  html, body {
    width: 1200px; height: 871px; overflow: hidden;
    background: var(--backdrop);
    font-family: "Noto Sans", Verdana, sans-serif;
  }
  .canvas {
    width: 1200px; height: 871px;
    display: flex; flex-direction: column;
    align-items: center; justify-content: center; gap: 44px;
  }
  .card {
    position: relative;
    width: 620px; height: 378px;
    background: radial-gradient(ellipse at 45% 45%, var(--card-light) 0%, var(--card-light) 35%, var(--card-shade) 100%);
    box-shadow: 0 6px 18px rgba(0,0,0,.28);
  }
  .brand-name {
    color: var(--brand-blue); font-weight: 700; line-height: 1;
  }
  .brand-line { color: var(--ink); line-height: 1.1; }

  /* back side */
  .card-back {
    display: flex; flex-direction: column; align-items: center;
    padding-top: 108px; text-align: center;
  }
  .card-back .brand-name { font-size: 30px; }
  .card-back .brand-line { font-size: 25px; margin-top: 2px; }
  .services-title { font-size: 19px; color: var(--ink); margin-top: 20px; }
  .services-list { font-size: 14px; color: var(--ink); margin-top: 8px; line-height: 1.45; }

  /* front side */
  .card-front .brand-block { position: absolute; left: 34px; top: 34px; }
  .card-front .brand-name { font-size: 31px; }
  .card-front .brand-line { font-size: 26px; margin-top: 4px; }
  .postal {
    position: absolute; left: 34px; top: 190px;
    font-size: 15px; color: var(--ink); line-height: 1.5;
  }
  .person { position: absolute; right: 34px; top: 190px; text-align: right; }
  .person-name { font-size: 23px; font-weight: 700; color: var(--brand-blue); line-height: 1.1; }
  .person-role { font-size: 16px; color: var(--ink); margin-top: 2px; }
  .contact {
    position: absolute; right: 34px; bottom: 34px;
    font-size: 17px; color: var(--ink); line-height: 1.55;
  }
  .contact-row { display: flex; align-items: center; justify-content: flex-end; gap: 10px; }
  .contact-icon { width: 20px; height: 16px; fill: var(--ink-soft); }
</style>
</head>
<body>
<main class="canvas">
  <section class="card card-back" aria-label="Card back">
    <div class="brand-name">Kestrel</div>
    <div class="brand-line">communications pty ltd</div>
    <div class="services-title">Service</div>
    <div class="services-list">
      Data | Phone | Cabling | Antennas<br>
      Fibre optics | Audio visual | Home theatre
    </div>
  </section>

  <section class="card card-front" aria-label="Card front">
    <div class="brand-block">
      <div class="brand-name">Kestrel</div>
      <div class="brand-line">communications pty ltd</div>
    </div>
    <div class="postal">
      kestrel communications pty ltd<br>
      PO BOX 657 Marlow Flats QLD 4873
    </div>
    <div class="person">
      <div class="person-name">Doug Pemberton</div>
      <div class="person-role">Director/Technician</div>
    </div>
    <div class="contact">
      <div class="contact-row">
        <span>043.719.6084</span>
        <svg class="contact-icon" viewBox="0 0 20 16" aria-hidden="true">
          <path d="M2 5c0-2 3-3 8-3s8 1 8 3v1h-4V4.5C13 4 7 4 6 4.5V6H2z"/>
          <path d="M5 7h10l2 7H3z"/>
        </svg>
      </div>
      <div class="contact-row">
        <span>kestrel4me@maildrop-example.com</span>
        <svg class="contact-icon" viewBox="0 0 20 16" aria-hidden="true">
          <path d="M1 2h18v12H1z M2.5 3.5 10 9l7.5-5.5" stroke="#fff" stroke-width="1"/>
        </svg>
      </div>
    </div>
  </section>
</main>
</body>
</html>
```